CuraNexa System Web Page Design

This project is to design 6 pages of a web based medical system for clinics, hospitals, drugs suppliers, general items suppliers, insurance company, laboratories and patients (basically all parties which could be involved in).We want the designs of the browser, button, icon and layout are based on Zolt, which is user friendly, looks professional, simple and neat but with powerful functions. We have uploaded few pictures of another system, please do not copy its design because this is not what we are looking for, the pictures are for you to know the elements should be included in our pages. CuraNexa web-base system, design 6 pages1. Login PageShould include the following elements-company id with input field-login id with input field-password with input field2. Main Page (Navigation page)Should include the following elements-Appointment-Consultation-Patient-Drugs inventory -General supplies inventory -Laboratory-Suppliers-Insurance-Reports 3. Appointment PageShould include all the the elements in the respective pictures plus the followings-Daily View, Weekly View, Monthly View buttons4. Consultation PageShould include all the the elements in the respective picture5. Patient Page5.1 General information Should include all the the elements in the respective picture5.2 medical history/lab reportsShould include all the the elements in the respective picture plus the followings-Notify patient button-Share report button.
Updated on 28 Nov:
Please stop using Ward Harbor in your designs which is not the name of our system. We have just rename our system to CuraNexa, please take note.
We need the system to look professional not playful, do not use too many colors and playful icons.
Target Market(s)
professional users
Number of Pages Required
5+ page
Look and feel

```html
<!DOCTYPE html>
<html lang="en">
<head>
<meta charset="utf-8">
<title>CuraNexa – Healthcare System</title>
<link href="https://fonts.googleapis.com/css2?family=Fira+Sans:wght@300;400;500;600;700&family=Roboto:wght@300;400;500;700&display=swap" rel="stylesheet">
<style>
:root{
  --teal:#11bcc7;
  --teal-dark:#0aa7b2;
  --orange:#f7a21b;
  --ink:#333333;
  --muted:#777777;
  --light:#f5f5f5;
  --line:#e4e4e4;
  --footer:#232323;
  --footer-text:#d6d6d6;
  --white:#ffffff;
}
*{margin:0;padding:0;box-sizing:border-box}
html,body{width:1200px;height:2624px;overflow:hidden;background:var(--white)}
body{position:relative;font-family:"Roboto",sans-serif;color:var(--ink)}
.abs{position:absolute}

/* top bar */
.topbar{left:0;top:0;width:1200px;height:28px;background:var(--teal);color:var(--white);font-size:11px}
.topbar .phone{left:161px;top:7px;display:flex;align-items:center;gap:6px}
.topbar .login{left:889px;top:0;width:73px;height:28px;background:var(--white);color:var(--ink);text-align:center;line-height:28px;font-size:11px}
.topbar .signup{left:962px;top:0;width:74px;height:28px;background:var(--orange);color:var(--white);text-align:center;line-height:28px;font-size:11px}

/* header */
.header{left:0;top:28px;width:1200px;height:84px;background:var(--white);box-shadow:0 1px 4px rgba(0,0,0,.08)}
.brand{left:161px;top:22px;display:flex;align-items:center;gap:8px;font-family:"Fira Sans",sans-serif;font-weight:700;font-size:34px;color:var(--teal)}
.brand .dot{width:22px;height:22px;border-radius:50%;background:var(--teal)}
.nav{left:520px;top:0;display:flex;height:84px;font-size:11px;text-transform:uppercase;color:#555}
.nav a{display:block;padding:0 12px;line-height:84px;text-decoration:none;color:inherit}
.nav a.active{background:var(--teal);color:var(--white);line-height:70px;height:56px;border-radius:0 0 4px 4px;margin-top:0}

/* hero */
.hero{left:0;top:112px;width:1200px;height:488px;background:linear-gradient(110deg,#c9d4d8 0%,#a9bcc2 45%,#b8c6cb 70%,#d0d9dc 100%)}
.hero-caption{left:315px;top:371px;width:572px;height:180px;background:rgba(255,255,255,.82);border:6px solid rgba(255,255,255,.5);text-align:center;padding-top:24px}
.hero-caption h1{font-family:"Fira Sans",sans-serif;font-weight:300;font-size:32px;color:#333}
.hero-caption h1 b{font-weight:600}
.hero-caption p{font-size:11.5px;color:#555;line-height:19px;margin:12px auto 0;width:460px}
.dots{display:flex;justify-content:center;gap:6px;margin-top:22px}
.dots span{width:10px;height:10px;border-radius:50%;border:1.5px solid var(--teal)}
.dots span.on{background:var(--teal);box-shadow:inset 0 0 0 2px #fff}

/* section titles */
.section-title{width:1200px;left:0;text-align:center;font-family:"Fira Sans",sans-serif;font-weight:400;font-size:27px;color:#333;display:flex;justify-content:center;align-items:center;gap:12px}
.section-title b{font-weight:600}
.section-title::before,.section-title::after{content:"";width:32px;height:2px;background:var(--teal)}
.section-lede{left:0;width:1200px;text-align:center;font-size:11.5px;line-height:20px;color:#777}

/* features */
.feature{display:flex;align-items:center;gap:18px;font-family:"Roboto",sans-serif;font-weight:500;font-size:13px;text-transform:uppercase;color:#333;height:38px;line-height:15px}
.feature svg{width:26px;height:26px;flex:none}
.feature.active{background:var(--teal);color:var(--white);width:203px}
.feature.active .ico{background:var(--orange);width:42px;height:38px;display:flex;align-items:center;justify-content:center}
.feature .ico{width:42px;display:flex;justify-content:center}
.monitor{left:406px;top:761px;width:388px;height:309px}
.monitor .screen{left:0;top:0;width:388px;height:244px;background:#1d1f24;border-radius:8px;padding:10px}
.monitor .display{width:368px;height:214px;background:linear-gradient(90deg,#2d2f36 0 18%,#f1f3f6 18% 100%)}
.monitor .chin{left:0;top:244px;width:388px;height:30px;background:#d7d9dc;border-radius:0 0 8px 8px}
.monitor .stand{left:150px;top:274px;width:88px;height:32px;background:linear-gradient(#c4c6c9,#e3e4e6);clip-path:polygon(15% 0,85% 0,100% 100%,0 100%)}

/* who we are */
.who-band{left:0;top:1125px;width:1200px;height:437px;background:var(--light)}
.who-photo{left:161px;top:1112px;width:354px;height:468px;background:var(--white);padding:8px;box-shadow:0 2px 8px rgba(0,0,0,.12)}
.who-photo .fill{width:100%;height:100%;background:linear-gradient(160deg,#c6ccd6,#e9ecf1 50%,#b7bfcb)}
.who-title{left:610px;top:1178px;display:flex;align-items:center;gap:12px;font-family:"Fira Sans",sans-serif;font-size:27px;color:#333}
.who-title::before{content:"";width:32px;height:2px;background:var(--teal)}
.who-title b{font-weight:600}
.who-lead{left:610px;top:1236px;width:430px;font-family:"Fira Sans",sans-serif;font-weight:500;font-size:16px;line-height:21px;color:#555}
.who-body{left:610px;top:1290px;width:430px;font-size:11px;line-height:19px;color:#777}
.who-body p{margin-bottom:16px}

/* contact band */
.contact-band{left:0;top:1562px;width:1200px;height:240px}
.contact-band .title{top:68px;color:var(--white)}
.contact-band .title::before,.contact-band .title::after{background:var(--white)}
.contact-band .lede{top:106px;color:var(--white)}

/* contact content */
.label{font-family:"Fira Sans",sans-serif;font-weight:600;font-size:16px;color:var(--teal);text-transform:uppercase}
.left-info{left:236px;top:1850px;width:236px}
.social{display:flex;gap:12px;margin-top:6px}
.social span{width:13px;height:13px;border-radius:50%;background:#b5b5b5}
.social span:first-child{background:var(--orange)}
.info-block{border-top:1px solid var(--line);margin-top:16px;padding-top:14px}
.info-block:first-of-type{border:none}
.info-block p{font-size:11px;line-height:16px;color:#888;margin-top:6px}
.form{left:610px;top:1850px;width:354px}
.form h3{font-family:"Fira Sans",sans-serif;font-weight:400;font-size:16px;color:#333;text-transform:uppercase}
.form h3 b{font-weight:600}
.form .note{font-size:11px;line-height:16px;color:#888;margin:8px 0 16px;width:290px}
.field{height:31px;background:#f2f2f2;font-size:11px;color:#999;display:flex;align-items:center;gap:8px;padding-left:10px;margin-bottom:6px}
.row{display:flex;gap:6px}
.row .field{flex:1}
.field.msg{height:78px;align-items:flex-start;padding-top:10px}
.btn-submit{width:84px;height:31px;background:var(--orange);color:var(--white);font-size:11px;font-weight:700;letter-spacing:1px;text-align:center;line-height:31px;margin-top:14px;border-radius:2px}

/* footer */
.footer{left:0;top:2211px;width:1200px;height:413px;background:var(--footer);color:var(--footer-text)}
.fcol{top:56px}
.fcol h4{font-family:"Fira Sans",sans-serif;font-weight:600;font-size:14px;color:var(--white)}
.fcol h4::after{content:"";display:block;width:24px;height:2px;background:var(--teal);margin-top:10px}
.fcol ul{list-style:none;margin-top:14px}
.fcol li{font-size:10.5px;line-height:26.2px;color:var(--footer-text)}
.fcol p{font-size:10.5px;line-height:22px;margin-top:14px}
.fcol .more{color:var(--orange);font-size:10.5px;margin-top:4px}
.subscribe{left:834px;top:2367px;width:205px}
.subscribe .input{height:30px;border:1px solid #999;font-size:10.5px;color:#ccc;display:flex;align-items:center;gap:8px;padding-left:10px}
.subscribe .go{width:76px;height:30px;background:var(--white);color:var(--teal-dark);font-size:10px;font-weight:700;letter-spacing:1px;text-align:center;line-height:30px;margin-top:14px}
.copyright{left:0;top:2576px;width:1200px;height:48px;border-top:1px solid #3a3a3a;font-size:10.5px;color:var(--footer-text)}
.copyright .l{left:161px;top:16px}
.copyright .l b{color:var(--teal);font-weight:400}
.copyright .r{left:876px;top:16px}
</style>
</head>
<body>

<div class="abs topbar">
  <div class="abs phone">
    <svg width="11" height="11" viewBox="0 0 24 24"><path d="M6.6 10.8a15 15 0 0 0 6.6 6.6l2.2-2.2c.3-.3.7-.4 1-.2 1.1.4 2.3.6 3.6.6.6 0 1 .4 1 1V20c0 .6-.4 1-1 1A17 17 0 0 1 3 4c0-.6.4-1 1-1h3.5c.6 0 1 .4 1 1 0 1.3.2 2.5.6 3.6.1.3 0 .7-.2 1z" fill="#fff"/></svg>
    Call Us: (555) 0142 7788
  </div>
  <div class="abs login">LOGIN</div>
  <div class="abs signup">SIGN UP</div>
</div>

<header class="abs header">
  <div class="abs brand"><span class="dot"></span>CuraNexa</div>
  <nav class="abs nav">
    <a class="active">Home</a><a>Appointment</a><a>Patient Info</a><a>Lab Reports</a><a>Consultation</a><a>Contact Us</a>
  </nav>
</header>

<section class="abs hero" role="img" aria-label="Photo of a patient's arm having blood pressure measured beside a stethoscope and clipboard"></section>
<div class="abs hero-caption">
  <h1>World class <b>Healthcare</b> where you live.</h1>
  <p>Lorem ipsum dolor sit amet, consectetur adipiscing elit, sed do eiusmod tempor incididunt ut labore et dolore magna aliqua. Ut enim ad minim veniam, quis nostrud exercitation</p>
  <div class="dots"><span></span><span class="on"></span><span></span></div>
</div>

<h2 class="abs section-title" style="top:650px">WHAT <b>WE DO</b></h2>
<p class="abs section-lede" style="top:687px">Lorem ipsum dolor sit amet, consectetur adipiscing elit, sed do eiusmod tempor incididunt ut labore et dolore magna aliqua.<br>Ut enim ad minim veniam, quis nostrud exercitation ullamco laboris nisi</p>

<div class="abs" style="left:161px;top:761px;display:flex;flex-direction:column;gap:22px">
  <div class="feature active"><span class="ico"><svg viewBox="0 0 24 24" fill="none" stroke="#fff" stroke-width="1.6"><rect x="3" y="5" width="18" height="16" rx="1"/><path d="M3 10h18M8 3v4M16 3v4M7 14h2M11 14h2M15 14h2M7 17h2M11 17h2"/></svg></span>Appointment</div>
  <div class="feature"><span class="ico"><svg viewBox="0 0 24 24" fill="none" stroke="#11bcc7" stroke-width="1.5"><rect x="4" y="10" width="16" height="9" rx="2"/><path d="M8 10V7a4 4 0 0 1 8 0v3M9 14h6"/></svg></span>Consultation</div>
  <div class="feature"><span class="ico"><svg viewBox="0 0 24 24" fill="none" stroke="#11bcc7" stroke-width="1.5"><path d="M3 18V8M3 14h18v4M8 14v-3h11a2 2 0 0 1 2 2v1"/><circle cx="6" cy="11" r="1.5"/></svg></span>Patient</div>
  <div class="feature"><span class="ico"><svg viewBox="0 0 24 24" fill="none" stroke="#11bcc7" stroke-width="1.5"><rect x="6" y="7" width="10" height="14" rx="1"/><path d="M7 3h8v4H7zM9 14h4M11 12v4"/><circle cx="18" cy="17" r="3"/></svg></span>Drugs Inventory</div>
  <div class="feature"><span class="ico"><svg viewBox="0 0 24 24" fill="none" stroke="#11bcc7" stroke-width="1.5"><path d="M4 20l4-4M7 17l9-9 3 3-9 9zM14 6l4 4M17 3l4 4"/></svg></span>General Supplies<br>Inventory</div>
</div>

<div class="abs monitor" role="img" aria-label="Desktop monitor showing the CuraNexa dashboard with statistics, charts and patient lists">
  <div class="abs screen"><div class="display"></div></div>
  <div class="abs chin"></div>
  <div class="abs stand"></div>
</div>

<div class="abs" style="left:835px;top:761px;display:flex;flex-direction:column;gap:22px">
  <div class="feature"><span class="ico"><svg viewBox="0 0 24 24" fill="none" stroke="#11bcc7" stroke-width="1.5"><path d="M9 3h6M10 3v6l-5 10a1.5 1.5 0 0 0 1.3 2h11.4a1.5 1.5 0 0 0 1.3-2L14 9V3M7 15h10"/></svg></span>Laboratory</div>
  <div class="feature"><span class="ico"><svg viewBox="0 0 24 24" fill="none" stroke="#11bcc7" stroke-width="1.5"><path d="M2 4h3l3 11h11l2-8H7"/><circle cx="9" cy="19" r="1.5"/><circle cx="17" cy="19" r="1.5"/></svg></span>Suppliers</div>
  <div class="feature"><span class="ico"><svg viewBox="0 0 24 24" fill="none" stroke="#11bcc7" stroke-width="1.5"><circle cx="10" cy="6" r="3"/><path d="M4 20v-4a6 6 0 0 1 10-4.5"/><path d="M17 12l4 1.5v3c0 2.5-2 4-4 4.5-2-.5-4-2-4-4.5v-3z"/></svg></span>Insurance</div>
  <div class="feature"><span class="ico"><svg viewBox="0 0 24 24" fill="none" stroke="#11bcc7" stroke-width="1.5"><rect x="5" y="4" width="14" height="17" rx="1"/><path d="M9 3h6v3H9zM8 11h8M8 14h8M8 17h5"/></svg></span>Reports</div>
</div>

<div class="abs who-band"></div>
<div class="abs who-photo"><div class="fill" role="img" aria-label="Photo of a doctor in a white coat with a stethoscope, cropped at the shoulders"></div></div>
<h2 class="abs who-title">WHO <b>WE ARE</b></h2>
<p class="abs who-lead">Sed ut perspiciatis unde omnis iste natus error sit volupta tem accusantium doloremque</p>
<div class="abs who-body">
  <p>laudantium, totam rem aperiam, eaque ipsa quae ab illo inventore veritatis et quasi architecto beatae vitae dicta sunt explicabo. Nemo enim ipsam voluptatem quia voluptas sit aspernatur aut odit aut fugit, sed quia consequuntur magni dolores eos qui ratione voluptatem sequi nesciunt. Neque porro quisquam est, qui dolorem ipsum quia dolor sit amet, consectetur, adipisci velit, sed quia non numquam eius modi tempora</p>
  <p>Ut enim ad minima veniam, quis nostrum exercitationem ullam corporis suscipit laboriosam, nisi ut aliquid ex ea commodi consequatur. Quis autem vel eum iure reprehenderit qui in ea voluptate velit esse quam nihil molestiae consequatur</p>
  <p>Duis aute irure dolor in reprehenderit in voluptate velit esse cillum dolore eu fugiat nulla pariatur. Excepteur sint occaecat cupidatat non proident,</p>
</div>

<section class="abs contact-band">
  <svg class="abs" style="left:0;top:0" width="1200" height="240" viewBox="0 0 1200 240" preserveAspectRatio="none">
    <path fill="#11bcc7" d="M0 0H1200V195C1170 175 1140 168 1110 180C1070 198 1040 168 1000 170C960 172 940 200 900 195C860 190 840 165 800 168C760 172 740 200 700 196C660 192 640 165 600 168C560 172 540 200 500 196C460 192 440 168 400 170C360 172 340 200 300 196C260 192 240 168 200 170C160 172 140 200 100 200C60 200 40 178 0 225Z"/>
  </svg>
  <h2 class="abs section-title title">CONTACT <b>US</b></h2>
  <p class="abs section-lede lede">Lorem ipsum dolor sit amet, consectetur adipiscing elit, sed do eiusmod tempor incididunt ut labore et dolore magna aliqua.<br>Ut enim ad minim veniam, quis nostrud exercitation ullamco laboris nisi</p>
</section>

<div class="abs left-info">
  <div class="info-block">
    <div class="label">Follow Us</div>
    <div class="social"><span></span><span></span><span></span><span></span></div>
  </div>
  <div class="info-block">
    <div class="label">Address</div>
    <p>Sed ut perspiciatis unde omnis iste natus<br>error sit voluptatem accusantium</p>
  </div>
  <div class="info-block">
    <div class="label">Contact Us</div>
    <p>+100 555 0199<br>hello@curanexa.test</p>
  </div>
</div>

<div class="abs form">
  <h3>Get in <b>Touch</b></h3>
  <p class="note">Please complete and submit this form and one of our representatives will reply promptly</p>
  <div class="row">
    <div class="field"><svg width="10" height="10" viewBox="0 0 24 24" fill="#aaa"><circle cx="12" cy="7" r="5"/><path d="M2 23c0-6 4-9 10-9s10 3 10 9z"/></svg>Your Name</div>
    <div class="field"><svg width="10" height="10" viewBox="0 0 24 24" fill="#aaa"><path d="M2 5h20v14H2z"/></svg>Your Email</div>
  </div>
  <div class="field"><svg width="10" height="10" viewBox="0 0 24 24" fill="#aaa"><path d="M5 2h10l4 4v16H5z"/></svg>Subject</div>
  <div class="field msg"><b style="color:#888">?</b>Message</div>
  <div class="btn-submit">SUBMIT</div>
</div>

<footer class="abs footer">
  <div class="abs fcol" style="left:161px;width:240px">
    <h4>About US</h4>
    <p>Lorem ipsum dolor sit amet, consectetur adipiscing elit, sed do eiusmod tempor incididunt ut labore et dolore magna aliqua. Ut enim ad minim veniam, quis nostrud exercitation ullamco laboris nisi ut aliquip ex ea commodo consequat. Duis aute irure dolor in reprehenderit in voluptate velit esse cillum dolore</p>
    <div class="more">Read More</div>
  </div>
  <div class="abs fcol" style="left:460px">
    <h4>Quick Links</h4>
    <ul><li>Home</li><li>Appointment</li><li>Patient Info</li><li>Lab Reports</li><li>Consultation</li><li>Contact Us</li></ul>
  </div>
  <div class="abs fcol" style="left:610px">
    <h4>Services</h4>
    <ul><li>Appointment</li><li>Consultation</li><li>Patient</li><li>Drugs inventory</li><li>General supplies inventory</li><li>Laboratory</li><li>Suppliers</li><li>Insurance</li><li>Reports</li></ul>
  </div>
  <div class="abs fcol" style="left:834px;width:205px">
    <h4>Subscribe Us</h4>
    <p style="line-height:16px">Subscribe to our Newsletter! to get latest news and updates regarding health</p>
  </div>
</footer>
<div class="abs subscribe">
  <div class="input"><svg width="11" height="11" viewBox="0 0 24 24" fill="none" stroke="#ccc" stroke-width="2"><path d="M2 5h20v14H2zM2 5l10 8 10-8"/></svg>Your email Address</div>
  <div class="go">SUBMIT</div>
</div>
<div class="abs copyright">
  <div class="abs l">© 2018 <b>CuraNexa</b>. All rights reserved.</div>
  <div class="abs r">Design By Brightlane Studio Inc.</div>
</div>

</body>
</html>
```